Buch-/eBook-Cover für Sachbuch gesucht
Zielgruppe
We're selfpublishing nonfiction books. Interested are adults - mostly man (age range: 25-50) - who want to learn more about leadership at their workplaces.
Aufgabenstellung
The design should be clean and simple, title easy to read, good color contrast (the cover has to stand out from an white background).

```html
<!DOCTYPE html>
<html lang="en">
<head>
<meta charset="utf-8">
<title>Mentorship – Book Cover</title>
<link rel="stylesheet" href="https://fonts.googleapis.com/css2?family=Oswald:wght@500;700&display=swap">
<style>
  :root {
    --page-bg: #ebebec;
    --gold-light: #ecd05a;
    --gold-mid: #ddb02a;
    --gold-deep: #b98a18;
    --gold-edge: #d9a91c;
    --ink: #151412;
  }
  * { margin: 0; padding: 0; box-sizing: border-box; }
  html, body {
    width: 1200px;
    height: 1200px;
    overflow: hidden;
    background: var(--page-bg);
  }
  .book-cover {
    position: absolute;
    left: 196px;
    top: 30px;
    width: 808px;
    height: 1140px;
    overflow: hidden;
    background:
      radial-gradient(ellipse 70% 45% at 85% 15%, var(--gold-light) 0%, rgba(236,208,90,0) 70%),
      linear-gradient(160deg, var(--gold-mid) 0%, #e3bb3a 35%, #d4a62a 65%, var(--gold-deep) 100%);
    font-family: "Oswald", "Arial Narrow", sans-serif;
    color: var(--ink);
    text-transform: uppercase;
  }
  .book-cover__fold {
    position: absolute;
    left: 36px;
    top: 0;
    width: 2px;
    height: 100%;
    background: var(--gold-edge);
    box-shadow: 1px 0 0 rgba(255,240,170,0.35);
  }
  .book-title,
  .book-subtitle,
  .book-author {
    position: absolute;
    left: 36px;
    right: 0;
    text-align: center;
    line-height: 1;
    white-space: nowrap;
  }
  .book-title {
    top: 234px;
    font-weight: 700;
    font-size: 134px;
    letter-spacing: -1px;
  }
  .book-subtitle {
    top: 398px;
    font-weight: 500;
    font-size: 36px;
    letter-spacing: 0.2px;
  }
  .book-author {
    top: 1028px;
    font-weight: 500;
    font-size: 28px;
  }
</style>
</head>
<body>
  <main class="book-cover">
    <div class="book-cover__fold"></div>
    <h1 class="book-title">Mentorship</h1>
    <p class="book-subtitle">Cultivating Trust and Unlocking Potential</p>
    <p class="book-author">Daniel Whitmore</p>
  </main>
</body>
</html>
```